Integrated Health Clinic brochure

We need a brochure designed to highlight the services that we offer at the integrated clinic. Please see "Our Services" of our website for description of services to be added to the brochure except for Acupuncture, which is described below:

"Acupuncture is an ancient Chinese methodology that has been proven to be very effective in many health issues, particularly in relieving pain. It involves the stimulation of acupuncture points on the body to regain the natural balance of the body. Medical Acupuncture is effective in treating a wide variety of conditions including: headaches, neck and back pains, carpal tunnel syndrome, fibromyalgia, asthma, allergies, sinus problems, digestive disorders and many others."

our motto "Relieve, Rejuvenate, Renew"

Services we provide:
Chiropractic
Physiotherapy
Family counselling
Massage Therapy
Acupuncture
Osteopath

Colors are blue and green.

See our website www.velmorahealth.ca

```html
<!DOCTYPE html>
<html lang="en">
<head>
<meta charset="utf-8">
<title>Velmora Health Wellness – Brochure</title>
<link href="https://fonts.googleapis.com/css2?family=Arimo:wght@400;700&family=Roboto:wght@100;300&display=swap" rel="stylesheet">
<style>
  :root {
    --green: #8cc63f;
    --blue: #2b7fc3;
    --text: #333333;
    --rule: #7aa6d6;
    --paper: #ffffff;
  }
  * { box-sizing: border-box; margin: 0; padding: 0; }
  html, body { width: 1200px; height: 927px; overflow: hidden; background: var(--paper); }
  .brochure { position: relative; width: 1200px; height: 927px; font-family: "Arimo", Arial, sans-serif; color: var(--text); }
  .panel { position: absolute; top: 0; width: 400px; height: 927px; }
  .panel--team { left: 0; }
  .panel--contact { left: 400px; border-left: 1px dashed var(--rule); border-right: 1px dashed var(--rule); }
  .panel--cover { left: 800px; }

  /* Team panel */
  .team-title { position: absolute; left: 23px; top: 176px; font-family: "Roboto", sans-serif; font-weight: 300; font-size: 34px; letter-spacing: -0.5px; color: var(--blue); }
  .team-title span { color: var(--green); }
  .member { position: absolute; left: 23px; right: 0; }
  .member-name, .member-role { display: flex; align-items: baseline; white-space: nowrap; }
  .member-name { font-size: 15px; color: var(--green); letter-spacing: 0.2px; }
  .member-role { font-size: 12px; color: var(--blue); margin-top: 9px; }
  .leader { flex: 1; border-bottom: 1px dashed var(--rule); margin-left: 2px; transform: translateY(-3px); }

  /* Contact panel */
  .map { position: absolute; left: 74px; top: 77px; width: 252px; height: 233px; background: linear-gradient(135deg, #ecebe6, #dcdad2 60%, #e8e6de); }
  .band { position: absolute; left: 0; width: 400px; }
  .band--blue { top: 370px; height: 7px; background: var(--blue); }
  .band--green { top: 377px; height: 6px; background: var(--green); }
  .address { position: absolute; left: 22px; top: 430px; font-size: 13.5px; line-height: 23px; letter-spacing: 0.3px; }
  .details { position: absolute; left: 22px; top: 541px; width: 220px; font-size: 11.5px; line-height: 18px; }
  .details p { margin-bottom: 5px; }
  .details strong { font-weight: 700; }

  .brand { position: absolute; display: flex; align-items: center; gap: 8px; font-family: "Arimo", Arial, sans-serif; font-size: 28px; color: #2d2d2d; letter-spacing: -0.5px; }
  .brand-mark { width: 22px; height: 22px; background: var(--green); border-radius: 50%; }
  .panel--contact .brand { left: 22px; top: 806px; }
  .panel--cover .brand { left: 233px; top: 331px; }

  /* Cover panel */
  .motto { position: absolute; left: 23px; top: 112px; font-family: "Roboto", sans-serif; font-weight: 100; font-size: 58px; line-height: 54px; letter-spacing: -1px; }
  .motto-line { display: flex; align-items: flex-end; }
  .motto-line svg { margin-left: 4px; margin-bottom: 8px; }
  .motto-line--green { color: var(--green); }
  .motto-line--blue { color: var(--blue); }
  .hero { position: absolute; left: 0; top: 395px; width: 400px; height: 532px;
    background:
      radial-gradient(circle at 20% 30%, #fff6d8 0%, rgba(255,236,170,0.7) 18%, rgba(255,230,170,0) 45%),
      linear-gradient(180deg, #e9c98a 0%, #c89a4e 45%, #8d8c3a 70%, #6c8a2a 100%); }
</style>
</head>
<body>
<div class="brochure">

  <section class="panel panel--team">
    <h2 class="team-title">OUR <span>TEAM</span></h2>

    <div class="member" style="top:254px">
      <div class="member-name">Dr. Owen Hartley B.A., D.C.<span class="leader"></span></div>
      <div class="member-role">Chiropractor, Active Release Techniques (ART) Provider</div>
    </div>
    <div class="member" style="top:345px">
      <div class="member-name">Dr. Renata Voss, D.C.<span class="leader"></span></div>
      <div class="member-role">Chiropractor and Contemporary Medical Acupuncturist</div>
    </div>
    <div class="member" style="top:436px">
      <div class="member-name">Marcus Dale, MSW, RSW<span class="leader"></span></div>
      <div class="member-role">Registered Social Worker</div>
    </div>
    <div class="member" style="top:526px">
      <div class="member-name">Petra Ellingham<span class="leader"></span></div>
      <div class="member-role">Registered Massage Therapist</div>
    </div>
    <div class="member" style="top:619px; left:22px">
      <div class="member-name">Iris Calder, DO(MP)<span class="leader"></span></div>
      <div class="member-role">Osteopath &amp; Certified Acupuncturist</div>
    </div>
    <div class="member" style="top:710px">
      <div class="member-name">Nora (Mei Lin) Sato</div>
      <div class="member-role">Certified Acupuncturist<span class="leader"></span></div>
    </div>
    <div class="member" style="top:800px">
      <div class="member-name">Priya Rameshan<span class="leader"></span></div>
      <div class="member-role">Physiotherapist</div>
    </div>
  </section>

  <section class="panel panel--contact">
    <div class="map" role="img" aria-label="Street map showing the clinic location near the subway station"></div>
    <div class="band band--blue"></div>
    <div class="band band--green"></div>

    <address class="address" style="font-style:normal">
      Velmora Health Wellness<br>
      1480 Larkfield Road, Suite 305,<br>
      Brenton, Ontario
    </address>

    <div class="details">
      <p><strong>1-866-555-0142</strong></p>
      <p><strong>Location:</strong></p>
      <p>Southeast corner of Larkfield Road and Mercer Avenue East.</p>
      <p><strong>Transit</strong> – Across from Mercer Subway station</p>
      <p><strong>PARKING</strong> – there is free 1 hour parking on Pellam Ave before 4 pm and there is a City Lot parking garage on Ashgrove Street and other parking garages nearby</p>
    </div>

    <div class="brand"><span class="brand-mark"></span>Velmora</div>
  </section>

  <section class="panel panel--cover">
    <h1 class="motto">
      <span class="motto-line motto-line--green">RELIEVE
        <svg width="22" height="16" viewBox="0 0 22 16"><path d="M1 8 L8 14 L21 1" fill="none" stroke="var(--green)" stroke-width="1.5"/></svg></span>
      <span class="motto-line motto-line--blue">REJUVENATE
        <svg width="22" height="16" viewBox="0 0 22 16"><path d="M1 8 L8 14 L21 1" fill="none" stroke="var(--blue)" stroke-width="1.5"/></svg></span>
      <span class="motto-line motto-line--green">RENEW
        <svg width="22" height="16" viewBox="0 0 22 16"><path d="M1 8 L8 14 L21 1" fill="none" stroke="var(--green)" stroke-width="1.5"/></svg></span>
    </h1>

    <div class="brand"><span class="brand-mark"></span>Velmora</div>

    <div class="hero" role="img" aria-label="Photo of a woman doing a handstand on sunlit grass in a park"></div>
  </section>

</div>
</body>
</html>
```